wine bottle label design

My girlfriend and I are getting married. We are sending out invitations, in a wine bottle. For that we need a label on the bottle.
Our names are Marlene & Henrik. We would like the C and K to somehow play a bigger part in the logo.
Also maybe with an Illustration (best if made as a drawing resembling the church we are getting married in) https://www.sangfolket.dk/index.php/kalender/83-uncategorised/148-gospelgudstjeneste-i-tarnholm-kirke.html

Logo Text

Bryllup den 27 april 2019, kl. 14:00 i Tarnholm Kirke

Font styles to use
Decorative

```html
<!DOCTYPE html>
<html lang="da">
<head>
<meta charset="utf-8">
<title>Bryllup – Marlene &amp; Henrik</title>
<link rel="stylesheet" href="https://fonts.googleapis.com/css2?family=Alex+Brush&family=Lora:ital@1&display=swap">
<style>
  :root {
    --backdrop: #f5e9d9;
    --label-light: #fbfaf8;
    --label-mid: #ece8e2;
    --ink: #3a2218;
    --accent: #c4161c;
    --ornament: #d9d2c8;
    --illustration: #d6d3cf;
  }
  * { box-sizing: border-box; margin: 0; padding: 0; }
  html, body {
    width: 1200px; height: 1200px; overflow: hidden;
    background: var(--backdrop);
  }
  .label {
    position: absolute; left: 340px; top: 150px;
    width: 520px; height: 900px;
    border-radius: 10px;
    overflow: hidden;
    box-shadow: 0 0 0 2px #5a4a40;
  }
  .label__pattern {
    position: absolute; inset: 0;
    background: radial-gradient(ellipse at 60% 40%, var(--label-light) 0%, var(--label-mid) 100%);
  }
  .label__flourish {
    position: absolute; left: 110px; top: 40px;
    width: 300px; height: 80px;
    border-radius: 40px;
    background: linear-gradient(90deg, transparent, #b9aca3 30%, #b9aca3 70%, transparent);
    opacity: .55;
  }
  .names {
    position: absolute; left: 0; right: 0; top: 110px;
    font-family: "Alex Brush", cursive;
    color: var(--ink);
    line-height: .9;
  }
  .names__first { display: block; font-size: 128px; text-align: center; }
  .names__second { display: block; font-size: 118px; padding-left: 70px; }
  .names__amp {
    font-family: "Alex Brush", cursive;
    color: var(--accent); font-size: 52px; vertical-align: middle; margin-left: 14px;
  }
  .details {
    position: absolute; left: 40px; right: 40px; top: 385px;
    font-family: "Lora", serif; font-style: italic;
    font-size: 34px; line-height: 1.3;
    color: var(--ink); text-align: center;
  }
  .church {
    position: absolute; left: 30px; top: 530px;
    width: 290px; height: 370px;
    background: linear-gradient(180deg, rgba(214,211,207,.25), var(--illustration));
    clip-path: polygon(38% 0, 62% 0, 62% 30%, 100% 45%, 100% 100%, 0 100%, 0 40%, 38% 30%);
  }
  .monogram {
    position: absolute; left: 50px; top: 740px;
    width: 220px; height: 120px;
    border-radius: 50%;
    background: radial-gradient(ellipse, rgba(58,34,24,.35), rgba(58,34,24,.08) 70%, transparent);
  }
</style>
</head>
<body>
  <section class="label">
    <div class="label__pattern" role="img" aria-label="Soft cream damask pattern covering the label"></div>
    <div class="label__flourish" role="img" aria-label="Dark leafy ornamental flourish above the names"></div>
    <h1 class="names">
      <span class="names__first">Marlene</span>
      <span class="names__second">Henrik<span class="names__amp">&amp;</span></span>
    </h1>
    <p class="details">Bryllup den<br>27 april 2019, kl.<br>14:00 i Tarnholm Kirke</p>
    <div class="church" role="img" aria-label="Pencil drawing of Tarnholm Kirke with its tower"></div>
    <div class="monogram" role="img" aria-label="Heart monogram ornament with the couple's initials"></div>
  </section>
</body>
</html>
```